Corvane Project Services - Flyer

Project Breif:
I need a single page A4 Capability Statement, which will be used to market our services to prospective clients, both in print and via email PDF.
It needs to look professional and should incorporate the elements I have uploaded into files, these include:
Capability Statement Text
Corvane Services Company Logo
Additional Logo’s (Tools We Use)
Glimmer Bay Pics can be cut into the page
I have included examples of capability statements as a guide to what i am looking for.
Regards
Derek
Engineering Consulting

```html
<!DOCTYPE html>
<html lang="en">
<head>
<meta charset="utf-8">
<title>Corvane Project Services – Capability Statement</title>
<link href="https://fonts.googleapis.com/css2?family=Poppins:ital,wght@0,300;0,400;0,500;0,600;0,700;1,300;1,400&display=swap" rel="stylesheet">
<style>
  :root {
    --ink: #2b2b2b;
    --body: #3a3a3a;
    --brand-blue: #2f6db5;
    --band-grey: #d9dadc;
    --rule-blue: #4a7fc0;
    --white: #ffffff;
  }
  * { margin: 0; padding: 0; box-sizing: border-box; }
  html, body { width: 901px; height: 1200px; overflow: hidden; background: var(--white); }
  body { font-family: 'Poppins', sans-serif; color: var(--body); }
  .flyer { position: relative; width: 901px; height: 1200px; background: var(--white); overflow: hidden; }

  .brand { position: absolute; left: 60px; top: 40px; width: 220px; text-align: center; }
  .brand-mark { width: 58px; height: 58px; border-radius: 50%; background: var(--brand-blue); margin: 0 auto 14px; }
  .brand-name { font-size: 17px; font-weight: 600; color: var(--ink); letter-spacing: 0.5px; line-height: 1.2; }

  .contact { position: absolute; right: 31px; top: 77px; text-align: right; font-size: 12.5px; line-height: 19px; }
  .contact .address { color: #555; }
  .contact .links { color: var(--brand-blue); }

  .hero { position: absolute; left: 0; top: 0; width: 901px; height: 560px; }
  .hero-copy { position: absolute; left: 45px; top: 222px; color: var(--white); }
  .hero-title { font-size: 43px; line-height: 55px; font-weight: 300; letter-spacing: -0.5px; }
  .hero-title strong { font-weight: 700; }
  .hero-sub { margin-top: 10px; font-size: 16.5px; line-height: 25px; font-style: italic; font-weight: 300; }

  .section-title { font-size: 22px; font-weight: 600; color: var(--ink); line-height: 28px; margin-bottom: 8px; }
  .col p { font-size: 12px; line-height: 18px; letter-spacing: -0.2px; text-align: justify; hyphens: auto; -webkit-hyphens: auto; margin-bottom: 5px; }
  .about { position: absolute; left: 41px; top: 584px; width: 373px; }
  .team { margin-top: 12px; }
  .team p { line-height: 19.5px; }
  .expertise { position: absolute; left: 465px; top: 584px; width: 406px; }
  .expertise-body { border-left: 6px solid var(--rule-blue); padding-left: 26px; }

  .services { position: absolute; left: 0; top: 869px; width: 901px; height: 267px; background: var(--band-grey); }
  .service { position: absolute; top: 22px; }
  .service-head { display: flex; align-items: flex-start; gap: 16px; height: 60px; }
  .service-head svg { flex: none; }
  .service-title { font-size: 22px; font-weight: 600; line-height: 26px; color: var(--ink); }
  .service ul { list-style: none; margin-top: 2px; }
  .service li { font-size: 13px; line-height: 15px; margin-bottom: 7px; padding-left: 8px; text-indent: -8px; color: var(--body); }
  .service li::before { content: "• "; }
  .plan { left: 41px; width: 260px; }
  .risk { left: 356px; width: 250px; }
  .cost { left: 662px; width: 220px; }
  .divider { position: absolute; top: 22px; width: 2px; height: 208px; background: var(--rule-blue); }

  .tools { position: absolute; left: 0; top: 1136px; width: 901px; height: 50px; display: flex; align-items: center; justify-content: space-around; padding: 0 40px; }
  .tool { display: flex; align-items: center; gap: 7px; font-size: 14px; font-weight: 600; }
  .tool .dot { width: 14px; height: 14px; }
  .tool-a { color: #c9302c; } .tool-a .dot { background: #c9302c; }
  .tool-b { color: #2e8b4a; } .tool-b .dot { background: #2e8b4a; }
  .tool-c { color: #333; } .tool-c .dot { background: #d9232e; border-radius: 50%; }
  .tool-d { color: #2f6db5; } .tool-d .dot { background: #2f6db5; }
  .tool-e { color: #1f4e6e; } .tool-e .dot { background: #1f4e6e; border-radius: 50%; }
  .footer-strip { position: absolute; left: 0; top: 1186px; width: 901px; height: 14px; background: linear-gradient(90deg, #2c5c9a, #3e87c9); }
</style>
</head>
<body>
<div class="flyer">

  <svg class="hero" viewBox="0 0 901 560" role="img" aria-label="Photograph of a business meeting with hands reviewing documents and charts, toned blue">
    <defs>
      <linearGradient id="heroPhoto" x1="0" y1="0" x2="1" y2="1">
        <stop offset="0" stop-color="#4f79ae"/>
        <stop offset="0.55" stop-color="#7097c9"/>
        <stop offset="1" stop-color="#a6bfdd"/>
      </linearGradient>
    </defs>
    <polygon points="420,135 903,135 903,505 518,552 213,552" fill="#6c93c6"/>
    <rect x="0" y="170" width="901" height="335" fill="url(#heroPhoto)"/>
    <polygon points="420,135 903,135 903,170 405,170" fill="#7ea2d0"/>
    <polygon points="240,505 518,505 518,552 213,552" fill="#6f95c6"/>
  </svg>

  <header>
    <div class="brand">
      <div class="brand-mark"></div>
      <div class="brand-name">Corvane Project Services</div>
    </div>
    <div class="contact">
      <div class="address">Corvane Project Services Limited, Kilbrenna, Co Cork, Ireland.</div>
      <div class="links">+353 (0)870 555 014 | info@corvaneservices.ie | www.corvaneservices.ie</div>
    </div>
  </header>

  <div class="hero-copy">
    <h1 class="hero-title">Leading <strong>Project Control Consultancy</strong><br>based in <strong>Co. Cork Ireland.</strong></h1>
    <p class="hero-sub">For over 20 years we have been helping our clients to deliver<br>complex projects and programs throughout mainland Europe.</p>
  </div>

  <section class="col about">
    <h2 class="section-title">About Us</h2>
    <p>Our goal is to make successful project delivery more achievable and repeatable. We are continually innovating, evolving and learning, utilizing the latest industry tools and techniques to deliver real value to our clients.</p>
    <p>We are passionate about empowering organisations to achieve their objectives, on time and on budget.</p>
    <div class="team">
      <h2 class="section-title">Our Team</h2>
      <p>We use highly experienced industry professionals who engage with our clients to deliver practical and innovative project control solutions.</p>
    </div>
  </section>

  <section class="col expertise">
    <h2 class="section-title">Our Expertise</h2>
    <div class="expertise-body">
      <p>For over 20 years we have been helping our clients to successfully deliver capital projects within the pharmaceutical and biotechnology sectors.</p>
      <p>During this time, we have worked closely with multinational healthcare companies and leading A&amp;E firms, on a variety of business-critical projects.</p>
      <p>Our experience and knowledge of project control gives our client’s unparalleled visibility of Cost, Schedule and Risk through the lifecycle of their projects.</p>
      <p style="margin-bottom:0">This visibility allows our clients to make timely informed decisions which increase efficiency and project performance.</p>
    </div>
  </section>

  <section class="services">
    <div class="service plan">
      <div class="service-head">
        <svg width="44" height="46" viewBox="0 0 44 46" aria-hidden="true">
          <rect x="3" y="7" width="38" height="36" rx="3" fill="none" stroke="#2b2b2b" stroke-width="4"/>
          <rect x="3" y="7" width="38" height="9" fill="#2b2b2b"/>
          <rect x="10" y="1" width="5" height="10" rx="2" fill="#2b2b2b"/>
          <rect x="29" y="1" width="5" height="10" rx="2" fill="#2b2b2b"/>
          <g fill="#2b2b2b">
            <rect x="9" y="20" width="5" height="4"/><rect x="17" y="20" width="5" height="4"/><rect x="25" y="20" width="5" height="4"/><rect x="33" y="20" width="4" height="4"/>
            <rect x="9" y="27" width="5" height="4"/><rect x="17" y="27" width="5" height="4"/><rect x="25" y="27" width="5" height="4"/><rect x="33" y="27" width="4" height="4"/>
            <rect x="9" y="34" width="5" height="4"/><rect x="17" y="34" width="5" height="4"/><rect x="25" y="34" width="5" height="4"/><rect x="33" y="34" width="4" height="4"/>
          </g>
        </svg>
        <h3 class="service-title">Planning and<br>Scheduling</h3>
      </div>
      <ul>
        <li>Tender Planning</li>
        <li>Interactive Planning / Pull Planning</li>
        <li>CPM Planning &amp; Scheduling</li>
        <li>Agile / Lean Planning Methodology</li>
        <li>Independent Schedule Quality Assessment</li>
        <li>Schedule Risk Analysis (Monte Carlo)</li>
        <li>Training</li>
      </ul>
    </div>
    <div class="divider" style="left:324px"></div>
    <div class="service risk">
      <div class="service-head">
        <svg width="44" height="50" viewBox="0 0 44 50" aria-hidden="true">
          <path d="M22 3 L40 10 V24 C40 36 32 44 22 47 C12 44 4 36 4 24 V10 Z" fill="none" stroke="#2b2b2b" stroke-width="4" stroke-linejoin="round"/>
          <path d="M13 25 L20 32 L32 18" fill="none" stroke="#2b2b2b" stroke-width="4" stroke-linecap="round" stroke-linejoin="round"/>
        </svg>
        <h3 class="service-title">Management<br>of Risk</h3>
      </div>
      <ul>
        <li>Risk Management Policies &amp; Procedures</li>
        <li>Risk Management Strategy</li>
        <li>Risk Registers</li>
        <li>Risk Response and Communication</li>
        <li>Cost &amp; Schedule Risk Analysis (Monte Carlo)</li>
        <li>Risk Management Training</li>
      </ul>
    </div>
    <div class="divider" style="left:630px"></div>
    <div class="service cost">
      <div class="service-head">
        <svg width="52" height="52" viewBox="0 0 52 52" aria-hidden="true">
          <circle cx="21" cy="21" r="17" fill="none" stroke="#2b2b2b" stroke-width="4"/>
          <line x1="33" y1="33" x2="47" y2="47" stroke="#2b2b2b" stroke-width="7" stroke-linecap="round"/>
          <text x="21" y="28" text-anchor="middle" font-family="Poppins, sans-serif" font-weight="700" font-size="20" fill="#2b2b2b">£</text>
        </svg>
        <h3 class="service-title">Cost<br>Control:</h3>
      </div>
      <ul>
        <li>Estimating &amp; Forecasting</li>
        <li>Earned Value Management</li>
        <li>Progress Reporting</li>
        <li>Cost Risk Analysis<br>(Monte Carlo)</li>
      </ul>
    </div>
  </section>

  <footer class="tools">
    <div class="tool tool-a"><span class="dot"></span>Keyline P6</div>
    <div class="tool tool-b"><span class="dot"></span>Tasker Project</div>
    <div class="tool tool-c"><span class="dot"></span>Ardent Planner</div>
    <div class="tool tool-d"><span class="dot"></span>Veltrix Gauge</div>
    <div class="tool tool-e"><span class="dot"></span>Riskwell</div>
  </footer>
  <div class="footer-strip"></div>

</div>
</body>
</html>
```